We are a printed circuit board manufacturer. Need a company professional web site to allow our potential customers to know more about our background, capability and our products. The web site will contain three languages, which are Chinese, English and Japanese. Our audience are mainly electronic companies that procure printed circuit boards. I have a word document that have all the required text in all three languages. The final design should communicate the impression that we embrace quality, trustworthiness and long term partnership business principles.
We should have sections that allow us to post pictures of our facilities.
I have added the three files in three different languages.
Some of the information is below:
Background
RVD Worldwide Limited (RVD) was set up in Hong Kong in 2007 by two Hong Kong entrepreneurs, Mr. Lok Fai Tam and Mr. Wai Ho. We acquired the single sided printed circuit board factory located in Dongguan City, Guangdong Province, China, from Valtor Corporation of the U.S. in 2007. In addition to RVD, Mr. Tam and Mr. Ho also own Brightrail Systems Company Limited, a semiconductor company based in Hong Kong since 1997 with a total investment of over US$100 million. Brightrail is engaged in the manufacturing of flexible substrates and MEMS assembly business.
RVD has been awarded TS 16949 and ISO14000 certificates since 2009 and 2004 respectively.
Business Principles
RVD Worldwide Limited strives to be a professional top notched printed circuit board supplier. We embrace four “EXCELLENCE” principles, namely, excellence in quality, excellence in prices, excellence in services and excellence in on time delivery.
We approach each customer with a long-term partnership view that delivers the lowest ownership costs and highest total values to our customers. We customize quotations and solutions in order to allow our customers to win more businesses. We believe by thinking from our customers’ points of view we will be able to create a WIN-WIN relationship.
Customers
Due to our excellent quality, services and production systems, RVD Worldwide Limited manage to service a number of large Japanese and US customers, which include:
Technical capability overview
Below is an overview of our current capability:
Target Market(s)
Electronic companies buyers
Industry/Entity Type
Business
Requirements
Must have
- Capability description
Should not have
- no cartoon

```html
<!DOCTYPE html>
<html lang="en">
<head>
<meta charset="utf-8">
<title>RVD Worldwide Limited</title>
<link rel="stylesheet" href="https://fonts.googleapis.com/css2?family=Arimo:wght@400;700&family=Marcellus&family=Michroma&family=Saira+Condensed:wght@500&display=swap">
<style>
:root{
  --teal:#0a7a64;
  --teal-dark:#06624f;
  --ink:#111;
  --body:#4a4a4a;
  --login:#f7c98a;
  --footer:#4b4b4b;
  --footer-text:#e6e6e6;
  --bar:#000;
  --submit:#a3132f;
}
*{margin:0;padding:0;box-sizing:border-box}
html,body{width:1200px;height:1000px;overflow:hidden;background:#fff;font-family:"Arimo",Arial,sans-serif;color:var(--ink)}
.canvas{position:relative;width:1200px;height:1000px}
.top-band{position:absolute;left:0;top:0;width:1200px;height:7px;background:var(--teal)}
.brand{position:absolute;left:108px;top:38px;display:flex;align-items:center;gap:8px}
.brand-mark{width:18px;height:18px;background:var(--teal)}
.brand-name{font-family:"Arimo",sans-serif;font-weight:700;font-size:19px;color:var(--teal)}
.phone{position:absolute;left:967px;top:66px;display:flex;align-items:center;gap:5px;font-size:12.5px;color:#111}
.nav{position:absolute;left:99px;top:99px;width:1002px;height:36px;background:linear-gradient(#0c8068,var(--teal-dark));border-radius:5px 5px 0 0}
.nav a{font-family:"Marcellus",serif;color:#fff;text-decoration:none;font-size:15.5px;letter-spacing:1px;position:absolute;top:9px}
.login{position:absolute;right:0;top:0;width:88px;height:36px;background:var(--login);border-radius:0 5px 0 0;display:flex;align-items:center;justify-content:center;gap:8px;font-weight:700;font-size:14px;color:#111}
.hero{position:absolute;left:99px;top:134px;width:1002px;height:304px;border:1px solid #9fc6bc;background:#f7f7f7;overflow:hidden}
.hero-photo{position:absolute;left:360px;top:0;width:642px;height:304px;background:linear-gradient(90deg,#f7f7f7 0%,#a7a7a7 12%,#4a4b50 26%,#6b6a6c 38%,#d2ccc6 50%,#7a4a34 62%,#d9b7a2 72%,#e9d2c4 84%,#ececec 100%)}
.hero-title{position:absolute;left:40px;top:30px;font-family:"Michroma",sans-serif;color:var(--teal)}
.hero-title .l1{font-size:27px;line-height:34px}
.hero-title .l2{font-size:26px;line-height:31px;margin-left:-4px}
.hero-title .l3{font-size:19px;line-height:28px;letter-spacing:13.5px}
.principles{position:absolute;left:34px;top:141px;list-style:none}
.principles li{display:flex;align-items:center;gap:7px;height:32.5px;font-family:"Saira Condensed",sans-serif;font-weight:500;font-size:22px;letter-spacing:.4px;color:var(--teal)}
.arrow{position:absolute;top:237px}
.welcome{position:absolute;left:108px;top:504px;width:534px}
.welcome h1{font-size:15px;font-weight:700;margin-bottom:12px}
.welcome p{font-size:11.4px;line-height:14.4px;color:var(--body);text-align:justify;margin-bottom:14px}
.contact{position:absolute;left:668px;top:491px;width:432px;height:181px;background:linear-gradient(180deg,#999 0%,#2a2a2a 45%,#141414 60%,#555 100%)}
.contact h2{position:absolute;left:18px;top:15px;color:#fff;font-size:16px;font-weight:700}
.field{position:absolute;background:#fff;border:2px solid var(--teal);border-radius:5px;font-size:10.5px;color:#555;padding:6px 6px}
.required{position:absolute;left:24px;top:157px;color:#fff;font-size:11.5px;font-weight:700}
.submit{position:absolute;left:344px;top:150px;width:78px;height:23px;background:linear-gradient(#c4203f,var(--submit));border-radius:4px;color:#fff;font-size:9.5px;font-weight:700;display:flex;align-items:center;justify-content:center;gap:5px}
.section-head{position:absolute;font-size:15.5px;font-weight:700}
.section-rule{position:absolute;height:2px;background:#111}
.industries{position:absolute;left:112px;top:716px;list-style:none;display:grid;grid-template-columns:141px 214px 160px;row-gap:9px}
.industries li{font-size:14.3px;height:18.5px;display:flex;gap:7px;align-items:center}
.industries li::before{content:"›";font-weight:700;font-size:15px}
.customers{position:absolute;left:670px;top:722px;width:422px;height:76px;border:1px solid #444;display:grid;grid-template-columns:1fr 1fr 1fr;align-items:center;text-align:center}
.cust{font-weight:700;font-size:16px;color:#1a3e8f;line-height:1.3}
.cust .sub{display:block;font-size:12px;color:#1a6b3a}
.footer{position:absolute;left:0;top:822px;width:1200px;height:145px;background:var(--footer);color:var(--footer-text)}
.footer h3{position:absolute;left:108px;top:11px;font-size:12px;font-weight:700;color:#fff}
.links{position:absolute;top:41px;list-style:none;font-size:10.5px}
.links li{height:18px;line-height:18px}
.links li::before{content:"▸";font-size:7px;display:inline-block;width:10px;vertical-align:1px}
.address{position:absolute;right:108px;top:13px;text-align:right;font-size:10.5px;line-height:18px;font-style:normal}
.address strong{font-size:12px;color:#fff}
.copyright{position:absolute;left:0;top:967px;width:1200px;height:33px;background:var(--bar);color:#fff;font-size:10.5px;font-weight:700;text-align:center;line-height:33px}
</style>
</head>
<body>
<div class="canvas">
  <div class="top-band"></div>

  <div class="brand"><span class="brand-mark"></span><span class="brand-name">RVD Worldwide Limited</span></div>

  <div class="phone">
    <svg width="30" height="24" viewBox="0 0 30 24"><ellipse cx="14" cy="13" rx="13" ry="10" fill="var(--teal)"/><path d="M10 8c0 5 4 9 9 9l2-2-3-2-2 1c-2-1-3-2-4-4l1-2-2-3z" fill="#fff"/></svg>
    <span><b>(</b>852) 2960 4418</span>
  </div>

  <nav class="nav">
    <a style="left:43px">HOME</a>
    <a style="left:160px">PRODUCTS</a>
    <a style="left:313px">SERVICES</a>
    <a style="left:452px">TECHNICAL CAPABILITIES</a>
    <a style="left:720px">CONTACT US</a>
    <div class="login">
      <svg width="18" height="22" viewBox="0 0 18 22"><path d="M4 10V6a5 5 0 0 1 10 0v4" fill="none" stroke="#777" stroke-width="2.5"/><rect x="1" y="10" width="16" height="12" rx="2" fill="#888"/></svg>
      <span>login</span>
    </div>
  </nav>

  <svg class="arrow" style="left:62px" width="34" height="90" viewBox="0 0 34 90"><path d="M30 0L4 45l26 45h-6L0 45 24 0z" fill="var(--teal)"/></svg>
  <svg class="arrow" style="left:1104px" width="34" height="90" viewBox="0 0 34 90"><path d="M4 0l26 45-26 45h6L34 45 10 0z" fill="var(--teal)"/></svg>

  <section class="hero">
    <div class="hero-photo" role="img" aria-label="Photo of a smiling professional woman in an office with two colleagues blurred behind her"></div>
    <div class="hero-title">
      <div class="l1">We embrace four</div>
      <div class="l2">”EXCELLENCE”</div>
      <div class="l3">PRINCIPLES</div>
    </div>
    <ul class="principles">
      <li><svg width="30" height="20" viewBox="0 0 30 20"><path d="M1 11l8 7L29 2 10 13z" fill="var(--teal)"/></svg>EXCELLENCE IN QUALITY</li>
      <li><svg width="30" height="20" viewBox="0 0 30 20"><path d="M1 11l8 7L29 2 10 13z" fill="var(--teal)"/></svg>EXCELLENCE IN PRICES</li>
      <li><svg width="30" height="20" viewBox="0 0 30 20"><path d="M1 11l8 7L29 2 10 13z" fill="var(--teal)"/></svg>EXCELLENCE IN SERVICES</li>
      <li><svg width="30" height="20" viewBox="0 0 30 20"><path d="M1 11l8 7L29 2 10 13z" fill="var(--teal)"/></svg>EXCELLENCE IN ON TIME DELIVERY</li>
    </ul>
  </section>

  <section class="welcome">
    <h1>WELCOME TO RVD WORLDWIDE LIMITED (RVD)</h1>
    <p>RVD Worldwide Limited strives to be a professional top notched printed circuit board supplier. We embrace four "EXCELLENCE" principles, namely, excellence in quality, excellence in prices, excellence in services and excellence in on time delivery.printed circuit board supplier. We embrace four "EXCELLENCE" principles, namely, excellence in quality, excellence in prices.</p>
    <p>RVD Worldwide Limited strives to be a professional top notched printed circuit board supplier. We embrace four "EXCELLENCE" principles, namely, excellence in quality, excellence in prices, excellence in services and excellence in on time delivery.printed circuit board supplier. We embrace four "EXCELLENCE" principles, namely, excellence in quality, excellence in prices.</p>
  </section>

  <section class="contact">
    <h2>HAVE A QUESTION ? TALK TO US</h2>
    <div class="field" style="left:20px;top:45px;width:189px;height:27px">Name *</div>
    <div class="field" style="left:20px;top:79px;width:189px;height:27px">Email *</div>
    <div class="field" style="left:20px;top:114px;width:189px;height:27px">Phone *</div>
    <div class="field" style="left:224px;top:45px;width:200px;height:97px;padding:5px 12px">Comments</div>
    <div class="required">* INDICATES REQUIRED</div>
    <div class="submit">SUBMIT <span>▸</span></div>
  </section>

  <h2 class="section-head" style="left:108px;top:685px">INDUSTRIES SERVED</h2>
  <div class="section-rule" style="left:99px;top:710px;width:200px"></div>
  <ul class="industries">
    <li>Automotive</li><li>Defense &amp; Aerospace</li><li>Defense &amp; Aerospace</li>
    <li>Medical</li><li>Computer Equipment</li><li>Computer Equipment</li>
    <li>Telecom</li><li>Electronic Companies</li><li>Electronic Companies</li>
  </ul>

  <h2 class="section-head" style="left:675px;top:685px">CUSTOMERS</h2>
  <div class="section-rule" style="left:670px;top:710px;width:200px"></div>
  <div class="customers">
    <div class="cust">NORVALE<span class="sub">Tenwick Engineering</span></div>
    <div class="cust" style="color:#222">KORIHA</div>
    <div class="cust">Delmaro<span class="sub">Asahara</span></div>
  </div>

  <footer class="footer">
    <h3>POPULAR LINKS</h3>
    <ul class="links" style="left:108px">
      <li>Sitemap</li><li>Circuit Boardas</li><li>Capabilities</li><li>Industries Served</li><li>About Us</li>
    </ul>
    <ul class="links" style="left:274px">
      <li>Contact Us</li><li>Resources</li><li>Service Center</li><li>News &amp; Events</li><li>Privacy Policy</li>
    </ul>
    <address class="address">
      <strong>RVD Worldwide Limited</strong><br>
      18/F Harbourline Tower<br>
      72 Kestrel Road<br>
      Wan Chai, HONG KONG<br>
      Telephone: (852)29604418<br>
      Fax: (852)29604419<br>
      Email: sales@rvdboard.example
    </address>
  </footer>
  <div class="copyright">COPYRIGHT © 2012 RVD WORLDWIDE LIMITED. ALL RIGHTS RESERVED</div>
</div>
</body>
</html>
```